Design our letter, business card, powerpoint and more

We have a logo and want a design for our business use. Letters (word template), business card (for printing) powerpoint presentation (template) and more.

```html
<!DOCTYPE html>
<html lang="en">
<head>
<meta charset="utf-8">
<title>Fjellbyg – Business Card</title>
<link rel="stylesheet" href="https://fonts.googleapis.com/css2?family=Nunito+Sans:wght@300;400;700;800&display=swap">
<style>
  :root {
    --backdrop: #e3e3e3;
    --card: #f6f6f6;
    --shadow: rgba(0, 0, 0, 0.28);
    --wordmark: #a09d9d;
    --ink: #3a3a3a;
    --ink-soft: #444444;
    --accent: #9fcfe2;
  }
  html, body {
    margin: 0;
    width: 1200px;
    height: 1200px;
    overflow: hidden;
    background: var(--backdrop);
    font-family: "Nunito Sans", sans-serif;
  }
  .stage { position: relative; width: 1200px; height: 1200px; }
  .card {
    position: absolute;
    left: 266px;
    width: 667px;
    height: 400px;
    background: var(--card);
    box-shadow: 4px 5px 6px var(--shadow);
  }
  .card--front { top: 157px; }
  .card--back { top: 643px; }

  .brand {
    position: absolute;
    display: flex;
    align-items: center;
    gap: 16px;
  }
  .brand__square {
    background: var(--accent);
    display: block;
  }
  .brand__name {
    font-weight: 800;
    color: var(--wordmark);
    letter-spacing: 0.5px;
    line-height: 1;
  }
  .card--front .brand { left: 150px; top: 180px; }
  .card--front .brand__square { width: 44px; height: 44px; }
  .card--front .brand__name { font-size: 58px; }

  .card--back .brand { left: 96px; top: 176px; gap: 10px; }
  .card--back .brand__square { width: 26px; height: 26px; }
  .card--back .brand__name { font-size: 28px; }

  .person { position: absolute; left: 320px; top: 70px; color: var(--ink); }
  .person__name {
    margin: 0;
    font-size: 34px;
    font-weight: 800;
    line-height: 1;
    letter-spacing: 0.2px;
  }
  .person__role {
    margin: 14px 0 0;
    font-size: 19px;
    font-weight: 400;
    color: var(--ink-soft);
    letter-spacing: 0.4px;
  }
  .contact {
    position: absolute;
    left: 323px;
    top: 188px;
    margin: 0;
    display: grid;
    grid-template-columns: 53px auto;
    row-gap: 8px;
    font-size: 19px;
    font-weight: 400;
    color: var(--ink-soft);
    letter-spacing: 0.4px;
    line-height: 25px;
  }
  .contact dt, .contact dd { margin: 0; }
  .contact__address { line-height: 25px; }
</style>
</head>
<body>
<div class="stage">
  <section class="card card--front">
    <div class="brand">
      <span class="brand__square"></span>
      <span class="brand__name">FJELLBYG</span>
    </div>
  </section>

  <section class="card card--back">
    <div class="brand">
      <span class="brand__square"></span>
      <span class="brand__name">FJELLBYG</span>
    </div>
    <div class="person">
      <h1 class="person__name">Eirik Haugvold</h1>
      <p class="person__role">Marketing Director</p>
    </div>
    <dl class="contact">
      <dt>T .</dt><dd>(+47) 458 30 917</dd>
      <dt>E .</dt><dd>eirik@fjellbyg.no</dd>
      <dt>Ad .</dt>
      <dd class="contact__address">DEPARTMENT BODØ<br>Sjøgata 24,<br>8006 Bodø</dd>
    </dl>
  </section>
</div>
</body>
</html>
```